Manufacturing company needs new business card.

I need a unique Business Card that will truly stand out. Nothing too busy. Simple is good, right? Not looking for a standard design either. No cookie cutter layout. I am just looking for something interesting and a bit different. Does't have to completely off the wall crazy, just not your run of the mill business card. Clean and modern with a touch of industrial.

Target Market(s)

Air conditioning industry, Architects, builders.

Industry/Entity Type

Business

Contact Information for Business Card

Details to be included on card are:

Peter Walsh
Managing Director

T: 1300 418 592
M: 0427 385 914
W: www.brandvalefabrication.com.au
E: peter.walsh@brandvalefabrication.com.au
A: 58 Harlow Lane, Sydney NSW 2000

Font styles to use
Sans Serif

Colors
0355a3
848484
fbfbfb

Requirements
Must have
• Card design must be landscape.

```html
<!DOCTYPE html>
<html lang="en">
<head>
<meta charset="utf-8">
<title>Brandvale Fabrication – Business Card</title>
<link rel="stylesheet" href="https://fonts.googleapis.com/css2?family=Ubuntu:wght@400;500;700&display=swap">
<style>
  :root {
    --brand-blue: #313f87;
    --brand-grey: #75777b;
    --text-grey: #555659;
    --card-white: #f7f7f7;
    --backdrop: #a9a7a8;
    --white: #ffffff;
  }
  html, body {
    margin: 0;
    padding: 0;
    width: 1200px;
    height: 1200px;
    overflow: hidden;
    background: var(--backdrop);
    font-family: "Ubuntu", sans-serif;
  }
  .canvas {
    position: relative;
    width: 1200px;
    height: 1200px;
  }
  .card {
    position: absolute;
    width: 712px;
    height: 420px;
    overflow: hidden;
  }
  .card-front {
    left: 238px;
    top: 117px;
    background: var(--brand-blue);
  }
  .card-back {
    left: 231px;
    top: 642px;
    background: var(--card-white);
  }
  .brand {
    position: absolute;
    display: flex;
    align-items: center;
    gap: 30px;
    white-space: nowrap;
  }
  .brand-square {
    display: block;
    flex: none;
  }
  .brand-name {
    font-weight: 500;
    letter-spacing: -0.5px;
  }
  .card-front .brand {
    left: 91px;
    top: 173px;
  }
  .card-front .brand-square {
    width: 76px;
    height: 76px;
    background: var(--white);
  }
  .card-front .brand-name {
    color: var(--white);
    font-size: 40px;
  }
  .wave {
    position: absolute;
    left: 0;
    top: 0;
  }
  .holder {
    position: absolute;
    right: 30px;
    top: 32px;
    text-align: right;
    color: var(--white);
  }
  .holder-name {
    font-size: 28px;
    font-weight: 700;
    line-height: 34px;
  }
  .holder-role {
    font-size: 16px;
    line-height: 22px;
  }
  .card-back .brand {
    left: 31px;
    top: 170px;
  }
  .card-back .brand-square {
    width: 64px;
    height: 64px;
    background: var(--brand-blue);
  }
  .card-back .brand-name {
    color: var(--brand-blue);
    font-size: 34px;
  }
  .contact-list {
    position: absolute;
    left: 30px;
    top: 290px;
    margin: 0;
    padding: 0;
    list-style: none;
    color: var(--text-grey);
    font-size: 17px;
  }
  .contact-list li {
    display: flex;
    align-items: center;
    gap: 17px;
    height: 23.5px;
  }
  .contact-list svg {
    width: 18px;
    height: 18px;
    fill: var(--brand-blue);
    flex: none;
  }
  .address {
    position: absolute;
    right: 30px;
    top: 337px;
    margin: 0;
    text-align: right;
    font-style: normal;
    color: var(--text-grey);
    font-size: 17px;
    line-height: 23.5px;
  }
</style>
</head>
<body>
<main class="canvas">

  <section class="card card-front" aria-label="Card front">
    <div class="brand">
      <span class="brand-square"></span>
      <span class="brand-name">Brandvale Fabrication</span>
    </div>
  </section>

  <section class="card card-back" aria-label="Card back">
    <svg class="wave" width="712" height="200" viewBox="0 0 712 200" aria-hidden="true">
      <path d="M0,0 H712 V156 C610,152 530,100 430,52 C330,8 150,2 0,44 Z" fill="var(--brand-blue)"/>
      <path d="M0,60 C150,14 330,18 440,66 C560,120 630,166 712,170 V188 C620,186 540,142 440,96 C340,52 150,42 0,88 Z" fill="var(--brand-grey)"/>
      <path d="M44,82 C180,42 330,40 450,92 C560,140 630,172 712,178" fill="none" stroke="var(--card-white)" stroke-width="2.5"/>
    </svg>

    <div class="holder">
      <div class="holder-name">Peter Walsh</div>
      <div class="holder-role">Managing Director</div>
    </div>

    <div class="brand">
      <span class="brand-square"></span>
      <span class="brand-name">Brandvale Fabrication</span>
    </div>

    <ul class="contact-list">
      <li>
        <svg viewBox="0 0 24 24" aria-hidden="true"><path d="M2 9c0-3 4-5 10-5s10 2 10 5v2h-5V8.5c-1.5-.6-3.2-.8-5-.8s-3.5.2-5 .8V11H2zM6 12l3-3h6l3 3v8H6zm6 2a2.5 2.5 0 1 0 0 5 2.5 2.5 0 0 0 0-5z"/></svg>
        <span>1300 418 592</span>
      </li>
      <li>
        <svg viewBox="0 0 24 24" aria-hidden="true"><path d="M7 1h10a2 2 0 0 1 2 2v18a2 2 0 0 1-2 2H7a2 2 0 0 1-2-2V3a2 2 0 0 1 2-2zm0 3v14h10V4zm5 15.5a1.2 1.2 0 1 0 0 2.4 1.2 1.2 0 0 0 0-2.4z"/></svg>
        <span>0427 385 914</span>
      </li>
      <li>
        <svg viewBox="0 0 24 24" aria-hidden="true"><path d="M12 2a10 10 0 1 0 0 20 10 10 0 0 0 0-20zm6.9 9h-3a15 15 0 0 0-1.3-6A8 8 0 0 1 18.9 11zM12 4.1c.9 1.3 1.7 3.6 1.9 6.9h-3.8C10.3 7.7 11.1 5.4 12 4.1zM9.4 5a15 15 0 0 0-1.3 6h-3A8 8 0 0 1 9.4 5zM5.1 13h3a15 15 0 0 0 1.3 6A8 8 0 0 1 5.1 13zM12 19.9c-.9-1.3-1.7-3.6-1.9-6.9h3.8c-.2 3.3-1 5.6-1.9 6.9zm2.6-.9a15 15 0 0 0 1.3-6h3a8 8 0 0 1-4.3 6z"/></svg>
        <span>www.brandvalefabrication.com.au</span>
      </li>
      <li>
        <svg viewBox="0 0 24 24" aria-hidden="true"><path d="M2 5h20v14H2zm2.5 2L12 12.5 19.5 7zM4 8.8V17l5-4.5zm16 0L15 12.5l5 4.5zM10.5 13.6 4.8 17h14.4l-5.7-3.4L12 14.8z"/></svg>
        <span>peter.walsh@brandvalefabrication.com.au</span>
      </li>
    </ul>

    <address class="address">58 Harlow Lane,<br>Sydney NSW 2000</address>
  </section>

</main>
</body>
</html>
```